Pellmoor Digital - WebSite Design and Hosting

Emphasis on Pellmoor Digital Website Development

Prioritize the development of the website for "pellmoordigital.example" as the first and foremost project.

Client-Friendly Website Request Process
** Design the website to facilitate easy interaction for small and medium-sized business (SMB) customers who require a website.
** Include a user-friendly form that allows my customers to submit their website requirements. This form should enable customers to:
** They can Upload images and logos related to their brand.
** They can Select brand colors that align with their identity.

Provide ample space for them to add extensive information about their business and services.

Extensive Portfolio Showcase
Build a portfolio section featuring a minimum of 300 website examples. These examples should be categorized and presented in a way that makes it convenient for potential clients to sort through and select as references for their own projects.

Summary:
In summary, the primary focus is on developing "pellmoordigital.example" as the initial project. The website should be user-friendly for SMB clients, offering a form for submitting detailed requirements, including image and logo uploads and brand color selection. Additionally, an extensive portfolio with 300 website examples should be presented for clients' reference and convenience.

Target Market(s)

Small Business Owners who need a local website

Industry/Entity Type

WebDesign and hosting (A marketing agency)

Coding

Coded - Design and coding required

Number of Pages Required

5+ page

Font styles to use
Sans Serif
Script

Colors
0054AA
0677BA
7BADD7
CADEEF
E8F1F8
FFF300
FFF600
FEFA6F
FFFEC7
FFFEE8

Requirements
Must have
• Black background! My customers need a form to pick a website design package, upload logo, brand colors and description. That input must be easy to submit to Makerfold to do the ProJet, we will add marketing services as well
Nice to have
• Step by step like explanaining to a 5th grader what the instructions are to get signed up. I want high tech state of the art - for SMB owners who may not be tech savvy

```html
<!DOCTYPE html>
<html lang="en">
<head>
<meta charset="utf-8">
<title>Pellmoor Digital</title>
<link href="https://fonts.googleapis.com/css2?family=Poppins:wght@400;500;600;700&display=swap" rel="stylesheet">
<style>
:root{
  --bg:#07090d;
  --bg-deep:#000;
  --yellow:#fff300;
  --white:#fff;
  --text:#e6e6e6;
}
*{box-sizing:border-box;margin:0;padding:0}
html,body{width:1200px;height:3682px;overflow:hidden}
body{background:var(--bg);font-family:'Poppins',sans-serif;color:var(--white);position:relative}
.abs{position:absolute}
.btn{position:absolute;background:var(--yellow);color:#000;font-weight:600;font-size:16px;border-radius:24px;display:flex;align-items:center;justify-content:center}
.band-services{left:0;top:680px;width:1200px;height:640px;background:radial-gradient(ellipse at 50% 50%,#141b24 0%,#07090d 70%)}
.band-portfolio{left:0;top:1890px;width:1200px;height:915px;background:linear-gradient(180deg,#07090d 0%,#0b1622 60%,#0a1420 100%)}
.band-form{left:0;top:2805px;width:1200px;height:877px;background:var(--bg-deep)}
.logo{left:97px;top:20px;font-size:31px;font-weight:600}
.nav a{position:absolute;top:34px;font-size:15px;color:var(--white);text-decoration:none}
.nav .active{color:var(--yellow);border-bottom:2px solid var(--yellow);padding-bottom:2px}
.hero-title{left:97px;top:245px;font-size:46px;font-weight:700;line-height:64px}
.hero-text{left:97px;top:382px;font-size:13.5px;line-height:31px;color:var(--text);width:440px}
.hero-visual{left:640px;top:160px;width:430px;height:430px;border-radius:50%;background:radial-gradient(circle at 45% 40%,#8a8a86 0%,#3a3a34 55%,#16160f 100%);border:6px solid #1e1e14}
.sec-title{left:0;width:1200px;text-align:center;font-size:27px;font-weight:600}
.sec-text{left:155px;width:890px;text-align:center;font-size:13.5px;line-height:31px;color:var(--text)}
.card{top:895px;width:321px;height:332px;border:2px solid var(--yellow);background:rgba(16,18,21,.85);text-align:center}
.card h3{margin-top:130px;font-size:17px;font-weight:500}
.card p{margin:14px 14px 0;font-size:13.5px;line-height:31px;color:var(--text)}
.card svg{position:absolute;left:128px;top:38px}
.about-frame{left:121px;top:1400px;width:437px;height:395px;border:3px solid var(--yellow)}
.photo{position:absolute}
.about-title{left:631px;top:1385px;font-size:30px;font-weight:600}
.about-text{left:631px;top:1440px;width:485px;font-size:13.5px;line-height:31px;color:var(--text)}
.field{position:absolute;background:#fff;border-radius:4px;color:#777;font-size:13.5px;padding:0 17px;display:flex;align-items:center;justify-content:space-between}
.foot-links a{position:absolute;top:3437px;font-size:15px;color:var(--white);text-decoration:none}
.icon-box{position:absolute;top:3501px;width:50px;height:50px;background:var(--yellow);display:flex;align-items:center;justify-content:center}
.contact-text{position:absolute;top:3515px;font-size:15px}
.copyright{left:0;top:3603px;width:1200px;text-align:center;font-size:14.5px}
</style>
</head>
<body>
<div class="abs band-services"></div>
<div class="abs band-portfolio"></div>
<div class="abs band-form"></div>

<header>
  <div class="abs logo">Pellmoor Digital</div>
  <nav class="nav">
    <a class="active" style="left:585px">Home</a>
    <a style="left:670px">About Us</a>
    <a style="left:775px">Services</a>
    <a style="left:876px">Portfolio</a>
  </nav>
  <div class="btn" style="left:968px;top:22px;width:133px;height:45px">Contact Us</div>
</header>

<section class="hero">
  <h1 class="abs hero-title">Welcome To<br>Pellmoor Digital</h1>
  <p class="abs hero-text">Lorem ipsum dolor sit amet, consectetur adipiscing elit, sed do eiusmod tempor incididunt ut labore et dolore aliqua.</p>
  <div class="btn" style="left:100px;top:462px;width:133px;height:46px">Get Started</div>
  <div class="abs hero-visual" role="img" aria-label="Responsive website mockups on desktop, laptop, tablet and phone"></div>
</section>

<section class="services">
  <h2 class="abs sec-title" style="top:740px">Our Services</h2>
  <p class="abs sec-text" style="top:798px">Lorem ipsum dolor sit amet, consectetur adipiscing elit, sed do eiusmod tempor incididunt ut labore et dolore magna aliqua. Ut enim ad minim veniam, quis nostrud exercitation ullamco laboris nisi ut aliquip ex ea commodo consequat.</p>
  <div class="abs card" style="left:97px">
    <svg width="64" height="64" viewBox="0 0 64 64" fill="none" stroke="var(--yellow)" stroke-width="2"><circle cx="22" cy="36" r="20" fill="#2a2a2a" stroke="none"/><rect x="16" y="2" width="40" height="30"/><path d="M16 10h40M22 16h12M22 22h20M40 16h10"/><rect x="22" y="28" width="30" height="24"/><path d="M30 58h14M37 52v6"/><rect x="48" y="40" width="12" height="20" rx="2"/></svg>
    <h3>Lorem ipsum dolor</h3>
    <p>Lorem ipsum dolor sit amet, consectetur adipiscing elit, sed do eiusmod tempor incididunt ut labore et dolore magna aliqua.</p>
  </div>
  <div class="abs card" style="left:439px">
    <svg width="64" height="64" viewBox="0 0 64 64" fill="none" stroke="var(--yellow)" stroke-width="2"><circle cx="22" cy="36" r="20" fill="#2a2a2a" stroke="none"/><rect x="16" y="2" width="40" height="30"/><path d="M16 10h40M22 16h12M22 22h20M40 16h10"/><rect x="22" y="28" width="30" height="24"/><path d="M30 58h14M37 52v6"/><rect x="48" y="40" width="12" height="20" rx="2"/></svg>
    <h3>Lorem ipsum dolor</h3>
    <p>Lorem ipsum dolor sit amet, consectetur adipiscing elit, sed do eiusmod tempor incididunt ut labore et dolore magna aliqua.</p>
  </div>
  <div class="abs card" style="left:780px">
    <svg width="64" height="64" viewBox="0 0 64 64" fill="none" stroke="var(--yellow)" stroke-width="2"><circle cx="22" cy="36" r="20" fill="#2a2a2a" stroke="none"/><rect x="16" y="2" width="40" height="30"/><path d="M16 10h40M22 16h12M22 22h20M40 16h10"/><rect x="22" y="28" width="30" height="24"/><path d="M30 58h14M37 52v6"/><rect x="48" y="40" width="12" height="20" rx="2"/></svg>
    <h3>Lorem ipsum dolor</h3>
    <p>Lorem ipsum dolor sit amet, consectetur adipiscing elit, sed do eiusmod tempor incididunt ut labore et dolore magna aliqua.</p>
  </div>
</section>

<section class="about">
  <div class="abs about-frame"></div>
  <div class="photo" style="left:107px;top:1387px;width:439px;height:395px;background:linear-gradient(135deg,#c9d2d8 0%,#8fa3b2 45%,#3d5f80 80%,#1d3550 100%)" role="img" aria-label="Person typing on a laptop showing a blog page"></div>
  <h2 class="abs about-title">About Us</h2>
  <p class="abs about-text">Sed ut perspiciatis unde omnis iste natus error sit voluptatem accusantium doloremque laudantium, totam rem aperiam, eaque ipsa quae ab illo inventore veritatis et quasi architecto beatae vitae dicta sunt explicabo. Nemo enim ipsam voluptatem quia voluptas sit aspernatur aut odit aut fugit, sed quia consequuntur magni dolores eos qui ratione voluptatem sequi nesciunt. Neque porro quisquam est, qui dolorem ipsum quia dolor sit amet, consectetur, adipisci velit, sed quia non numquam eius modi tempora incidunt ut labore et dolore magnam aliquam quaerat voluptatem.</p>
  <div class="btn" style="left:631px;top:1742px;width:132px;height:45px">Read More</div>
</section>

<section class="portfolio">
  <h2 class="abs sec-title" style="top:1965px">Project Portfolio</h2>
  <div class="photo" style="left:98px;top:2056px;width:317px;height:193px;background:linear-gradient(135deg,#6b5a48,#d9d5cc 55%,#8a8070)" role="img" aria-label="Website wireframe sketch on a desk monitor"></div>
  <div class="photo" style="left:98px;top:2276px;width:317px;height:338px;background:linear-gradient(90deg,#3a3a3a 0%,#5c5c5c 30%,#e8e6df 55%,#f0d84a 100%)" role="img" aria-label="Open company brochure layout"></div>
  <div class="photo" style="left:441px;top:2056px;width:317px;height:279px;background:linear-gradient(135deg,#e3e6ea,#b9c9da 50%,#6d95c2)" role="img" aria-label="Website wireframe elements in perspective"></div>
  <div class="photo" style="left:441px;top:2360px;width:317px;height:254px;background:linear-gradient(180deg,#dfe3e6 0%,#eef0f1 65%,#b88d62 100%)" role="img" aria-label="Desktop monitor with a website layout on a wooden desk"></div>
  <div class="photo" style="left:784px;top:2056px;width:317px;height:336px;background:linear-gradient(90deg,#e8703a 0%,#d94a3c 35%,#f3eee8 60%,#2f5d8c 100%)" role="img" aria-label="Website template pages in red and blue"></div>
  <div class="photo" style="left:784px;top:2420px;width:317px;height:194px;background:linear-gradient(135deg,#f2f2ef,#c3cfd8 50%,#e7d9a8)" role="img" aria-label="Designer desk with a website on a monitor"></div>
  <div class="btn" style="left:534px;top:2663px;width:132px;height:46px">View More</div>
</section>

<section class="form">
  <h2 class="abs sec-title" style="top:2876px;font-size:31px">Get Started</h2>
  <div class="field" style="left:182px;top:2949px;width:411px;height:49px">Name</div>
  <div class="field" style="left:606px;top:2949px;width:411px;height:49px">Select brand colors <svg width="10" height="6"><path d="M0 0h10L5 6z" fill="#555"/></svg></div>
  <div class="field" style="left:182px;top:3011px;width:411px;height:49px">Upload images <svg width="13" height="13"><rect x="0.5" y="0.5" width="12" height="12" rx="2" fill="#555"/><path d="M4 9l5-5M5 4h4v4" stroke="#fff" stroke-width="1.3" fill="none"/></svg></div>
  <div class="field" style="left:606px;top:3011px;width:411px;height:49px">Select logos Brand <svg width="13" height="13"><rect x="0.5" y="0.5" width="12" height="12" rx="2" fill="#555"/><path d="M4 9l5-5M5 4h4v4" stroke="#fff" stroke-width="1.3" fill="none"/></svg></div>
  <div class="field" style="left:182px;top:3073px;width:835px;height:86px;align-items:flex-start;padding-top:12px;border-radius:8px">Message</div>
  <div class="btn" style="left:531px;top:3183px;width:136px;height:50px">Submit</div>
</section>

<footer>
  <div class="abs sec-title" style="top:3366px;font-size:32px">Pellmoor Digital</div>
  <nav class="foot-links">
    <a style="left:345px">Home</a>
    <a style="left:437px">About Us</a>
    <a style="left:551px">Services</a>
    <a style="left:660px">Portfolio</a>
    <a style="left:768px">Contact Us</a>
  </nav>
  <div class="icon-box" style="left:139px"><svg width="24" height="18"><rect width="24" height="18" rx="2" fill="#000"/><path d="M1 2l11 8 11-8" stroke="var(--yellow)" stroke-width="2" fill="none"/></svg></div>
  <div class="contact-text" style="left:212px">info@pellmoordigital.example</div>
  <div class="icon-box" style="left:490px"><svg width="18" height="24"><path d="M9 0a9 9 0 0 1 9 9c0 7-9 15-9 15S0 16 0 9a9 9 0 0 1 9-9z" fill="#000"/><circle cx="9" cy="9" r="3.5" fill="var(--yellow)"/></svg></div>
  <div class="contact-text" style="left:557px">Pellmoor Digital,United State.</div>
  <div class="icon-box" style="left:848px"><svg width="22" height="22" viewBox="0 0 24 24"><path d="M6.6 10.8a15 15 0 0 0 6.6 6.6l2.2-2.2a1 1 0 0 1 1-.25 11.4 11.4 0 0 0 3.6.57 1 1 0 0 1 1 1V20a1 1 0 0 1-1 1A17 17 0 0 1 3 4a1 1 0 0 1 1-1h3.5a1 1 0 0 1 1 1c0 1.25.2 2.45.57 3.57a1 1 0 0 1-.25 1z" fill="#000"/></svg></div>
  <div class="contact-text" style="left:917px">+1 555 0142 880</div>
  <p class="abs copyright">Copyrights@2023.Pellmoor Digital.All Rights Reserved</p>
</footer>
</body>
</html>
```